Pell Nutrition Therapy needs a business card design

I need a business card design for my private practice. Green is my favorite color. I would like the back of the card to include an area for future appointment dates and time. I provide nutrition therapy to individuals, groups and families. I work a lot with adolescents and women who have eating disorders, but also work with athletes.

Reason: I received several new designs and would like to take some time reviewing them.

Target Market(s)

I am working primarily with women, but also men (mostly athletes). I work with a lot of runners. I work with people who are 14-60's.

Industry/Entity Type

Nutrition

Font styles to use
Serif
Sans Serif

Colors
9bcb3c
acd037

Requirements
Nice to have
• I would love to have 'Pell' incorporated into the design since it is my last name. If possible, I'd love to have an actual moon if it looks professional.

A picture of food could also be on the card if it is simple, but not sure how it would look with Pell. I am open to ideas for both Pell and a picture of a food item.

Other font style are fine as long as they are easy to read.

```html
<!DOCTYPE html>
<html lang="en">
<head>
<meta charset="utf-8">
<title>Pell Nutrition Therapy – Business Card</title>
<link href="https://fonts.googleapis.com/css2?family=Tinos&display=swap" rel="stylesheet">
<style>
  :root {
    --backdrop: #3a3d42;
    --card-green: #99ff00;
    --ink: #ffffff;
    --ink-faded: rgba(255,255,255,0.45);
    --shadow: rgba(40,60,0,0.55);
    --moon-core: rgba(240,255,220,0.55);
    --moon-edge: rgba(220,255,170,0.25);
  }
  html, body {
    margin: 0; padding: 0;
    width: 1200px; height: 1000px;
    overflow: hidden;
    background: var(--backdrop);
  }
  .canvas { position: relative; width: 1200px; height: 1000px; font-family: "Tinos", "Times New Roman", serif; color: var(--ink); }
  .card {
    position: absolute;
    width: 812px; height: 463px;
    background: var(--card-green);
    border-radius: 22px;
    overflow: hidden;
  }
  .card-front { left: 18px; top: 18px; }
  .card-back { left: 363px; top: 512px; }
  .moon {
    position: absolute;
    border-radius: 50%;
    background: radial-gradient(circle at 50% 50%, var(--moon-core) 0%, var(--moon-core) 60%, var(--moon-edge) 100%);
  }
  .card-front .moon { left: 220px; top: 30px; width: 410px; height: 410px; }
  .card-back .moon { left: 218px; top: 20px; width: 420px; height: 420px; }
  .line { position: absolute; left: 0; right: 0; text-align: center; line-height: 1; text-shadow: 1px 2px 2px var(--shadow); white-space: nowrap; }
  .practice-name { font-size: 66px; line-height: 0.9; top: 22px; left: 10px; }
  .person-name { font-size: 42px; top: 198px; left: 10px; }
  .credentials { font-size: 33px; top: 244px; left: 10px; }
  .contact { font-size: 28px; left: 10px; display: flex; justify-content: center; align-items: center; gap: 10px; }
  .contact svg { width: 28px; height: 28px; flex: none; }
  .contact-address { top: 332px; }
  .contact-email { top: 362px; }
  .contact-phone { top: 392px; }
  .contact-fax { top: 421px; }
  .back-text { position: absolute; line-height: 1; white-space: nowrap; }
  .back-brand { left: 25px; top: 20px; font-size: 44px; color: var(--ink-faded); }
  .back-heading { left: 25px; top: 72px; font-size: 46px; }
  .col-label { top: 130px; font-size: 46px; transform: translateX(-50%); }
  .col-date { left: 207px; }
  .col-divider { left: 397px; font-size: 40px; top: 130px; transform: translateX(-50%); }
  .col-time { left: 603px; }
  .write-lines { position: absolute; left: 0; top: 0; width: 812px; height: 463px; }
</style>
</head>
<body>
<main class="canvas">
  <section class="card card-front">
    <div class="moon" role="img" aria-label="Soft full moon photograph behind the text"></div>
    <div class="line practice-name">Pell Nutrition<br>Therapy</div>
    <div class="line person-name">Dara Whitfield Pell</div>
    <div class="line credentials">MS, RD, LDN</div>
    <div class="line contact contact-address">
      <svg viewBox="0 0 28 28" aria-hidden="true"><path d="M3 14 L14 4 L25 14 M6 12 V25 H22 V12" fill="none" stroke="#fff" stroke-width="2.5"/><rect x="11" y="17" width="6" height="8" fill="#fff"/></svg>
      <span>4471 Larkspur Lane, Brookvale, TN 37000</span>
    </div>
    <div class="line contact contact-email">
      <svg viewBox="0 0 28 28" aria-hidden="true"><circle cx="14" cy="14" r="11" fill="none" stroke="#fff" stroke-width="2.5"/><path d="M3 14 H25 M14 3 C8 9 8 19 14 25 C20 19 20 9 14 3" fill="none" stroke="#fff" stroke-width="2"/></svg>
      <span>dpell@brookmail.net</span>
    </div>
    <div class="line contact contact-phone">
      <svg viewBox="0 0 28 28" aria-hidden="true"><path d="M3 10 C3 5 25 5 25 10 L21 12 L18 9 H10 L7 12 Z" fill="#fff"/><rect x="6" y="14" width="16" height="10" rx="2" fill="#fff"/></svg>
      <span>555.014.2271</span>
    </div>
    <div class="line contact contact-fax">
      <svg viewBox="0 0 28 28" aria-hidden="true"><rect x="8" y="3" width="12" height="9" fill="none" stroke="#fff" stroke-width="2"/><rect x="4" y="13" width="20" height="11" fill="#fff"/></svg>
      <span>555.014.2290</span>
    </div>
  </section>

  <section class="card card-back">
    <div class="moon" role="img" aria-label="Soft full moon photograph behind the appointment area"></div>
    <div class="back-text back-brand">Pell Nutrition Therapy</div>
    <div class="back-text back-heading">Your Next Appointment:</div>
    <div class="back-text col-label col-date">Date</div>
    <div class="back-text col-divider">|</div>
    <div class="back-text col-label col-time">Time</div>
    <svg class="write-lines" viewBox="0 0 812 463" aria-hidden="true">
      <g stroke="#fff" stroke-width="4" stroke-linecap="round" stroke-dasharray="0 9.5">
        <line x1="30" y1="234" x2="310" y2="234"/><line x1="505" y1="234" x2="785" y2="234"/>
        <line x1="30" y1="304" x2="310" y2="304"/><line x1="505" y1="304" x2="785" y2="304"/>
        <line x1="30" y1="373" x2="310" y2="373"/><line x1="505" y1="373" x2="785" y2="373"/>
        <line x1="30" y1="440" x2="310" y2="440"/><line x1="505" y1="440" x2="785" y2="440"/>
      </g>
    </svg>
  </section>
</main>
</body>
</html>
```